Dune Air & Plus business card

I need an awesome, double-sided business card designed with our new logo. I would like the one side black with the colored logo, and the back side is all yours. I'd like to see horizontal and vertical layouts. Get creative! Thank you.

Target Market(s)

HVAC, Heating and Cooling in Phoenix, AZ

Industry/Entity Type

HVAC

Contact Information for Business Card

We need our new logo on the card. Tom Harker, (623) 555-0142, tom@trydunesair.com, www.trydunesair.com, ROC 514273

```html
<!DOCTYPE html>
<html lang="en">
<head>
<meta charset="utf-8">
<title>Dune Air &amp; Plus — Business Card</title>
<link rel="stylesheet" href="https://fonts.googleapis.com/css2?family=Montserrat:wght@400;500;700;800&display=swap">
<style>
  :root {
    --backdrop: #8a7458;
    --card-white: #ffffff;
    --card-dark: #1f1f1f;
    --orange: #e8622a;
    --orange-light: #f4a23a;
    --brand-blue: #1f74c4;
    --text-dark: #222222;
    --text-light: #ffffff;
  }
  * { box-sizing: border-box; margin: 0; padding: 0; }
  html, body {
    width: 900px; height: 1200px; overflow: hidden;
    background: var(--backdrop);
    font-family: "Montserrat", Arial, sans-serif;
  }
  .canvas { position: relative; width: 900px; height: 1200px; }
  .card {
    position: absolute; left: 80px; width: 742px; height: 440px;
    border-radius: 36px; overflow: hidden;
    box-shadow: 0 6px 14px rgba(0,0,0,0.35);
  }
  .card-front { top: 132px; background: var(--card-white); }
  .card-back { top: 638px; background: var(--card-dark); }

  .identity { position: absolute; left: 47px; top: 58px; }
  .identity-name { color: var(--orange); font-weight: 700; font-size: 25px; line-height: 1.1; }
  .identity-title { color: var(--text-dark); font-size: 16px; margin-top: 4px; }

  .brand-name {
    position: absolute; color: var(--brand-blue);
    font-weight: 800; text-align: center; white-space: nowrap;
  }
  .card-front .brand-name { left: 410px; width: 300px; top: 104px; font-size: 34px; line-height: 1.2; }
  .card-back .brand-name { left: 0; width: 742px; top: 200px; font-size: 54px; line-height: 1; }
  .brand-mark {
    display: block; width: 22px; height: 22px; border-radius: 50%;
    background: var(--orange); margin: 0 auto 14px;
  }
  .card-back .brand-mark { width: 32px; height: 32px; margin-bottom: 20px; }

  .license-tab {
    position: absolute; left: 0; top: 258px; width: 250px; height: 45px;
    background: linear-gradient(90deg, var(--orange), var(--orange-light));
    clip-path: polygon(0 0, 86% 0, 100% 100%, 0 100%);
    color: var(--text-dark); font-size: 15px;
    padding-left: 38px; line-height: 51px;
  }
  .contact-band {
    position: absolute; left: 0; top: 303px; width: 100%; height: 137px;
    background: var(--card-dark);
  }
  .contact-list { list-style: none; position: absolute; left: 38px; top: 36px; }
  .contact-list li {
    display: flex; align-items: center; gap: 13px;
    color: var(--text-light); font-size: 15.5px; height: 25px;
  }
  .contact-list svg { width: 16px; height: 16px; fill: var(--orange); }
</style>
</head>
<body>
<div class="canvas">

  <section class="card card-front">
    <div class="identity">
      <p class="identity-name">Tom Harker</p>
      <p class="identity-title">CEO &amp; Founder</p>
    </div>
    <div class="brand-name"><span class="brand-mark"></span>Dune Air &amp; Plus</div>
    <div class="license-tab">ROC 514273</div>
    <div class="contact-band">
      <ul class="contact-list">
        <li>
          <svg viewBox="0 0 16 16" aria-hidden="true"><path d="M2 5c0-2 2-3 6-3s6 1 6 3v1h-3V5H5v1H2z M4 8l2-2h4l2 2v5H4z M8 8.5a1.8 1.8 0 1 0 0 3.6a1.8 1.8 0 1 0 0-3.6z"/></svg>
          (623) 555-0142
        </li>
        <li>
          <svg viewBox="0 0 16 16" aria-hidden="true"><path d="M1 3h14v2L8 9 1 5z M1 6.5l7 4 7-4V13H1z"/></svg>
          tom@trydunesair.com
        </li>
        <li>
          <svg viewBox="0 0 16 16" aria-hidden="true"><path d="M8 1a7 7 0 1 0 0 14A7 7 0 1 0 8 1z M4 4l3 1 1 3-2 1-1 3-1-2-1-3z M10 9l3 1-2 3-2-1z" fill-rule="evenodd"/></svg>
          www.trydunesair.com
        </li>
      </ul>
    </div>
  </section>

  <section class="card card-back">
    <div class="brand-name"><span class="brand-mark"></span>Dune Air &amp; Plus</div>
  </section>

</div>
</body>
</html>
```